Automotive Business Card Design

I would just like a automotive themed card. nothing too extravagant, but catchy.

needs to say something about doing roadside assistance,mobile repairs, Diesel repairs, and Fleet maintenance

it can be single sided or double sided. no preference there.

Industry/Entity Type

Automotive

Contact Information for Business Card

Dana Whitcombe
phone 547 391 2084
Name: Brightway Automotive & Diesel Repair

```html
<!DOCTYPE html>
<html lang="en">
<head>
<meta charset="utf-8">
<title>Brightway Automotive &amp; Diesel Repair – Business Card</title>
<link rel="stylesheet" href="https://fonts.googleapis.com/css2?family=Michroma&display=swap">
<style>
  :root {
    --bg: #e9eaec;
    --card: #ffffff;
    --card-shade: #f1f2f4;
    --ink: #2f3237;
    --ink-soft: #55595f;
    --brand-blue: #1f7fd6;
    --band-light: #3ea6ee;
    --band-deep: #2a48c9;
    --band-edge: #6f7378;
  }
  * { box-sizing: border-box; margin: 0; padding: 0; }
  html, body {
    width: 1200px; height: 900px; overflow: hidden;
    background: var(--bg);
    font-family: "Michroma", "Trebuchet MS", sans-serif;
    color: var(--ink);
  }
  .canvas {
    width: 1200px; height: 900px;
    display: flex; flex-direction: column; align-items: center; justify-content: center;
    gap: 40px;
  }
  .card {
    position: relative;
    width: 700px; height: 400px;
    background: linear-gradient(135deg, var(--card) 0%, var(--card) 55%, var(--card-shade) 100%);
    box-shadow: 0 6px 18px rgba(0,0,0,.15);
    overflow: hidden;
  }
  .brand {
    display: flex; align-items: center; gap: 16px;
    position: absolute;
  }
  .brand-dot {
    width: 46px; height: 46px; border-radius: 50%;
    background: var(--brand-blue);
    flex: none;
  }
  .brand-name {
    color: var(--brand-blue);
    font-size: 17px; line-height: 1.35;
    letter-spacing: .04em;
    font-variant: small-caps;
  }
  .card-back .brand { left: 120px; top: 150px; }
  .services {
    position: absolute; left: 0; right: 0; top: 236px;
    text-align: center;
    font-size: 9px; letter-spacing: .08em; font-variant: small-caps;
    color: var(--ink-soft);
    white-space: nowrap;
  }
  .card-front .brand { left: 170px; top: 70px; }
  .person {
    position: absolute; left: 240px; top: 160px;
    font-size: 15px; letter-spacing: .08em; font-variant: small-caps;
    color: var(--ink);
    white-space: nowrap;
  }
  .person .divider { display: inline-block; width: 1px; height: 18px; background: var(--ink); margin: 0 10px; vertical-align: -3px; }
  .person .role { color: var(--ink-soft); }
  .contacts {
    position: absolute; left: 26px; top: 258px;
    font-size: 7.5px; letter-spacing: .04em; color: var(--ink-soft);
    font-variant: small-caps;
    line-height: 2.4;
    white-space: nowrap;
  }
  .contact-row { display: flex; gap: 10px; align-items: center; }
  .contact-item { display: inline-flex; align-items: center; gap: 4px; }
  .icon { width: 10px; height: 10px; flex: none; }
  .band { position: absolute; inset: 0; }
</style>
</head>
<body>
<main class="canvas">

  <section class="card card-back" aria-label="Card back">
    <div class="brand">
      <span class="brand-dot"></span>
      <span class="brand-name">Brightway Automotive<br>&amp; Diesel Repair</span>
    </div>
    <p class="services">Roadside Assistance · Mobile Repairs · Diesel Repairs · Fleet Maintenance</p>
  </section>

  <section class="card card-front" aria-label="Card front">
    <svg class="band" width="700" height="400" viewBox="0 0 700 400">
      <defs>
        <linearGradient id="bandFill" x1="0" y1="1" x2="1" y2="0">
          <stop offset="0" stop-color="var(--band-deep)"/>
          <stop offset=".55" stop-color="var(--band-light)"/>
          <stop offset="1" stop-color="var(--band-deep)"/>
        </linearGradient>
        <path id="bandCurve" d="M200,432 Q500,392 700,267"/>
      </defs>
      <path d="M190,400 Q495,355 700,228 L700,400 Z" fill="var(--band-edge)"/>
      <path d="M204,400 Q500,362 700,238 L700,400 Z" fill="url(#bandFill)"/>
      <text font-family="Michroma, sans-serif" font-size="13" letter-spacing="2" fill="#ffffff">
        <textPath href="#bandCurve" startOffset="36%">www.Brightwayrepair.com</textPath>
      </text>
    </svg>

    <div class="brand">
      <span class="brand-dot"></span>
      <span class="brand-name">Brightway Automotive<br>&amp; Diesel Repair</span>
    </div>

    <p class="person">Dana Whitcombe<span class="divider"></span><span class="role">Owner / C.E.O</span></p>

    <div class="contacts">
      <div class="contact-row">
        <span class="contact-item">
          <svg class="icon" viewBox="0 0 12 12"><circle cx="6" cy="6" r="6" fill="var(--ink-soft)"/><path d="M6,2.5 L9,5.5 H8 V9 H4 V5.5 H3 Z" fill="#fff"/></svg>
          Suite # 118, Harlow Bldg, NY 12408
        </span>
        <span class="contact-item">
          <svg class="icon" viewBox="0 0 12 12"><circle cx="6" cy="6" r="6" fill="var(--ink-soft)"/><circle cx="6" cy="6" r="3.4" fill="none" stroke="#fff" stroke-width="1"/><path d="M2.6,6 H9.4 M6,2.6 V9.4" stroke="#fff" stroke-width="1"/></svg>
          www.Brightwayrepair.com
        </span>
        <span class="contact-item">
          <svg class="icon" viewBox="0 0 12 12"><circle cx="6" cy="6" r="6" fill="var(--ink-soft)"/><rect x="3" y="4" width="6" height="4.2" fill="none" stroke="#fff" stroke-width="1"/><path d="M3,4 L6,6.4 L9,4" fill="none" stroke="#fff" stroke-width="1"/></svg>
          dana@brightwayrepair.com
        </span>
      </div>
      <div class="contact-row">
        <span class="contact-item">
          <svg class="icon" viewBox="0 0 12 12"><circle cx="6" cy="6" r="6" fill="var(--ink-soft)"/><path d="M4,3 L5.3,3 L5.8,4.8 L5,5.4 Q5.8,7 7,7.4 L7.6,6.6 L9,7.1 L9,8.4 Q5.5,8.8 3.6,4.4 Z" fill="#fff"/></svg>
          547-391-2084
        </span>
        <span class="contact-item">
          <svg class="icon" viewBox="0 0 12 12"><circle cx="6" cy="6" r="6" fill="var(--ink-soft)"/><rect x="4.2" y="2.6" width="3.6" height="6.8" rx=".6" fill="#fff"/></svg>
          318-604-2297
        </span>
        <span class="contact-item">
          <svg class="icon" viewBox="0 0 12 12"><circle cx="6" cy="6" r="6" fill="var(--ink-soft)"/><rect x="3" y="5" width="6" height="3.6" fill="#fff"/><rect x="4" y="3" width="4" height="2" fill="none" stroke="#fff" stroke-width=".8"/></svg>
          318-604-2298
        </span>
      </div>
    </div>
  </section>

</main>
</body>
</html>
```